Luxury Ayurvedic Hair Oil logo and package design

We need a logo and package design for our Ayurvedic and natural hair growth oil. Our company, Velmora, is the premier luxury Ayurvedic beauty brand, bringing ancient East-Indian natural and botanic health and beauty products to the US market. Our first major product - Velmora Hair Growth Oil - is a coconut oil based product that was developed by tribes in the Southern State of Kerala that includes ancient herbs like Gooseberry, Indigo, Indian Aloe, Balloon Vine and Brahmi.

The design should be catered to the high-end luxury market (minimal design, minimal text, fonts that invoke a sense of luxury). The primary colors should be deep blue for the packaging and gold for the characters (it's in the name - Velmora). We are looking to sell our products in Brenvale and Tolland Pryce and require packaging that is in line with products sold at these high-end retailers.

The final logo design and packaging should communicate luxury and the ancient wisdom of far-eastern traditions.

Target Market(s)

Velmora's main target is women who value fashionable/quality skincare, beauty, and fragrance products and are open to a medium to high price range. These women love uniqueness in brand and products that cannot be found elsewhere. They are looking for the next new "it" item that will take their haircare and beauty regiment to the next level.

Industry/Entity Type

Hair And Beauty

Font styles to use
Serif

Colors
2f73b3
ffc214

Requirements
Must have
• Must use deep blue (royal blue) background and gold text (to align with brand name). Must use luxurious fonts
Nice to have
• Flowers or other natural symbols, pictures that blend well with the product theme

```html
<!DOCTYPE html>
<html lang="en">
<head>
<meta charset="utf-8">
<title>Velmora Hair Growth Oil – Label</title>
<link href="https://fonts.googleapis.com/css2?family=Marcellus&family=Archivo+Narrow:wght@400;700&display=swap" rel="stylesheet">
<style>
  :root {
    --backdrop: #232323;
    --royal: #05057a;
    --gold: #a8800f;
    --gold-light: #f6c843;
    --white: #ffffff;
    --ink: #111111;
  }
  * { box-sizing: border-box; margin: 0; padding: 0; }
  html, body { width: 1200px; height: 657px; overflow: hidden; background: var(--backdrop); }
  .canvas { position: relative; width: 1200px; height: 657px; }
  .label {
    position: absolute; left: 88px; top: 88px; width: 1023px; height: 480px;
    background: var(--royal); overflow: hidden;
    font-family: "Marcellus", serif;
    box-shadow: 0 10px 30px rgba(0,0,0,.5);
  }
  .label-shapes { position: absolute; inset: 0; }
  .side-panel { position: absolute; left: 27px; color: var(--royal); }
  .side-heading { font-size: 23px; line-height: 1; }
  .side-copy { font-size: 13.5px; line-height: 17px; margin-top: 10px; width: 250px; }
  .ingredients-panel { top: 58px; }
  .usage-panel { top: 189px; }
  .notice-box {
    position: absolute; left: 27px; top: 290px; width: 270px; height: 62px;
    border: 2px solid var(--royal); color: var(--royal);
    font-size: 13.5px; line-height: 17px; text-align: center; padding-top: 4px;
  }
  .brand-mark { position: absolute; left: 412px; top: 44px; display: flex; align-items: center; gap: 12px; }
  .brand-dot { width: 64px; height: 64px; border-radius: 50%; background: var(--white); }
  .brand-name { color: var(--gold-light); line-height: 1; }
  .brand-name .word { font-size: 32px; display: block; }
  .brand-name .line { font-size: 17px; display: block; margin-top: 4px; border-bottom: 2px solid var(--gold-light); padding-bottom: 3px; }
  .product-title { position: absolute; left: 410px; top: 160px; color: var(--white); line-height: 1; }
  .product-title .main { font-size: 116px; letter-spacing: 1px; display: block; }
  .product-title .sub { font-size: 43px; display: block; margin-top: -4px; letter-spacing: -.5px; }
  .base-band {
    position: absolute; left: 371px; top: 307px; width: 300px; height: 33px;
    background: var(--gold); border-radius: 0 18px 18px 0;
    color: var(--white); font-size: 25px; letter-spacing: 1px; padding-left: 41px; line-height: 34px;
  }
  .herbs { position: absolute; left: 412px; top: 356px; color: var(--white); font-size: 16.5px; line-height: 20px; }
  .volume-band {
    position: absolute; left: 416px; top: 422px; width: 212px; height: 60px;
    background: var(--gold); border-radius: 0 60px 0 0;
    color: var(--white); font-size: 25px; text-align: center; padding: 14px 0 0 50px;
  }
  .nutrition {
    position: absolute; left: 731px; top: 35px; width: 258px; height: 356px;
    background: var(--white); border: 3px solid var(--ink); padding: 4px 8px;
    font-family: "Archivo Narrow", sans-serif; color: var(--ink); font-size: 10.5px;
  }
  .nutrition h2 { font-size: 31px; font-weight: 700; line-height: 1.1; letter-spacing: -.3px; }
  .serving { line-height: 14px; padding-bottom: 6px; border-bottom: 5px solid var(--ink); }
  .nf-row { display: flex; justify-content: space-between; border-bottom: 1px solid var(--ink); line-height: 14px; padding-top: 1px; }
  .nf-row.bold { font-weight: 700; }
  .nf-row.thick { border-bottom-width: 3px; }
  .nf-row.indent { padding-left: 12px; }
  .nf-row.right { justify-content: flex-end; font-size: 9px; }
  .nf-note { font-size: 6.5px; line-height: 8px; margin-top: 4px; }
  .extra-ingredients { position: absolute; left: 731px; top: 404px; width: 260px; color: var(--white); font-size: 10.5px; line-height: 13.5px; }
</style>
</head>
<body>
<div class="canvas">
  <div class="label">
    <svg class="label-shapes" width="1023" height="480" viewBox="0 0 1023 480" aria-hidden="true">
      <defs>
        <linearGradient id="ribbon-gold" x1="0" y1="0" x2="0.4" y2="1">
          <stop offset="0" stop-color="#f7c93a"/>
          <stop offset="0.4" stop-color="#fff6d6"/>
          <stop offset="0.75" stop-color="#e2b54a"/>
          <stop offset="1" stop-color="#b88a1c"/>
        </linearGradient>
      </defs>
      <path fill="#ffffff" d="M0,0 L138,0 C230,20 300,100 303,186 C306,290 380,400 481,480 L0,480 Z"/>
      <path fill="url(#ribbon-gold)" d="M138,0 L241,0 C320,40 365,110 368,186 C372,300 420,400 501,480 L481,480 C380,400 306,290 303,186 C300,100 230,20 138,0 Z"/>
      <path fill="none" stroke="#05057a" stroke-width="2" d="M138,0 C230,20 300,100 303,186 C306,290 380,400 481,480"/>
    </svg>

    <div class="side-panel ingredients-panel">
      <h3 class="side-heading">Ingredients:</h3>
      <p class="side-copy">Lorem ipsum dolor sit amet, consectetuer adipiscing elit, sed diam nonummy nibh euismod tincidunt ut laoreet dolore magna aliquam erat volutpat.</p>
    </div>
    <div class="side-panel usage-panel">
      <h3 class="side-heading">How to use:</h3>
      <p class="side-copy">Lorem ipsum dolor sit amet, consectetuer adipiscing elit, sed diam nonummy nibh euismod tincidunt ut.</p>
    </div>
    <div class="notice-box">Lorem ipsum dolor sit amet, consectetuer adipiscing elit, sed diam nonummy nibh euismod tincidunt.</div>

    <div class="brand-mark">
      <span class="brand-dot"></span>
      <span class="brand-name"><span class="word">Velmora</span><span class="line">Hair Growth Oil</span></span>
    </div>

    <h1 class="product-title"><span class="main">HAIR</span><span class="sub">GROWTH OIL</span></h1>
    <div class="base-band">COCONUT OIL</div>
    <p class="herbs">Gooseberry, Indigo, Indian Aloe,<br>Balloon Vine and Brahmi</p>
    <div class="volume-band">50ml</div>

    <div class="nutrition">
      <h2>Nutrition Facts</h2>
      <div class="serving">Serving Size 1 cup (300g)<br>Servings Per Container 5</div>
      <div class="nf-row" style="padding-top:5px">Amount Per Serving</div>
      <div class="nf-row bold thick"><span>Calories 358</span><span>Calories from Fat 90</span></div>
      <div class="nf-row right">% Daily Value</div>
      <div class="nf-row"><span><b>Total Fat</b> 5%</span><span>15%</span></div>
      <div class="nf-row indent"><span>Saturated Fat 1.7%</span><span>25%</span></div>
      <div class="nf-row indent"><span>Trans Fat 1%</span><span>5%</span></div>
      <div class="nf-row"><span><b>Cholesterol</b> 50mg</span><span>29%</span></div>
      <div class="nf-row"><span><b>Sodium</b> 300mg</span><span>17%</span></div>
      <div class="nf-row"><span><b>Total Carbohydrate</b> 10g</span><span>11%</span></div>
      <div class="nf-row indent"><span>Dietary Fiber 2g</span><span>5%</span></div>
      <div class="nf-row indent"><span>Sugars 3g</span><span></span></div>
      <div class="nf-row thick"><span><b>Protein</b> 10%</span><span></span></div>
      <div class="nf-row bold"><span>Vitamin A 1%</span><span>Vitamin C 3%</span></div>
      <div class="nf-row bold"><span>Calcium 3%</span><span>Iron 1%</span></div>
      <p class="nf-note">*Percent Daily Values are based on a 2,000 calorie diet. Your daily values may be higher or lower depending on your calorie needs.</p>
    </div>
    <p class="extra-ingredients">Ingredients: Lorem ipsum dolor sit amet, consectetuer adipiscing elit, sed diam nonummy nibh euismod tincidunt.</p>
  </div>
</div>
</body>
</html>
```